Velvet & Bloom Hair Extensions needs a business card

We need a business card designed for an online luxury hair extensions business called Velvet & Bloom, we already have a logo and need an innovative business card (2-sided preferably). The strap line for the brand is 'Premium Hair For Every Moment!'. The brand is a premium brand selling virgin hair extensions and the target market is the mid-affluent ethnic woman as such the design should reflect this. The brand logo is grey and can be sent when requested.

Target Market(s)

25 to 35 year mid-affluent ethnic woman (Afro-American, Mixed Race, Asian)

Industry/Entity Type

Hair

Colors

Designer to choose colors to be used in the design.

Requirements
Must have
• Business Name: Velvet and Bloom
Strapline: Premium Hair For Every Moment!
Domain: ​www.velvetandbloom-demo.com
Email: info@velvetandbloom-demo.com
sales and enquiries
44 07391 xxxxxxx

Please use the grey main brand logo depicted in page 2 of the attached pdf document

```html
<!DOCTYPE html>
<html lang="en">
<head>
<meta charset="utf-8">
<title>Velvet &amp; Bloom Hair Extensions – Business Card</title>
<link href="https://fonts.googleapis.com/css2?family=Questrial&display=swap" rel="stylesheet">
<style>
  :root {
    --pink: #ff0f5b;
    --grey: #a3a3a5;
    --white: #ffffff;
    --purple-light: #4b2270;
    --purple-mid: #2c1344;
    --purple-deep: #12081c;
    --value-bg: rgba(18, 8, 26, 0.85);
    --edge-dark: #0a0510;
  }
  html, body {
    margin: 0;
    padding: 0;
    width: 1200px;
    height: 741px;
    overflow: hidden;
    background: #ffffff;
  }
  .card {
    position: relative;
    width: 1200px;
    height: 741px;
    overflow: hidden;
    background: radial-gradient(ellipse 70% 75% at 50% 35%, var(--purple-light) 0%, var(--purple-mid) 50%, var(--purple-deep) 100%);
    font-family: "Questrial", "Century Gothic", sans-serif;
  }
  .card__frame {
    position: absolute;
    inset: 0;
    width: 1200px;
    height: 741px;
  }
  .brand-name {
    position: absolute;
    margin: 0;
    color: var(--grey);
    font-weight: 400;
    letter-spacing: 2px;
    white-space: nowrap;
    line-height: 1;
  }
  .brand-name--header {
    left: 500px;
    top: 128px;
    font-size: 62px;
  }
  .brand-mark {
    position: absolute;
    left: 112px;
    top: 560px;
    display: flex;
    align-items: center;
    gap: 18px;
  }
  .brand-mark__dot {
    width: 54px;
    height: 54px;
    border-radius: 50%;
    background: var(--grey);
  }
  .brand-mark .brand-name {
    position: static;
    font-size: 50px;
  }
  .tagline {
    position: absolute;
    left: 498px;
    top: 331px;
    width: 600px;
    height: 37px;
    background: var(--pink);
    color: var(--white);
    font-size: 24px;
    letter-spacing: 1px;
    line-height: 37px;
    text-align: center;
    margin: 0;
    white-space: nowrap;
  }
  .contact {
    position: absolute;
    left: 498px;
    top: 383px;
    margin: 0;
    padding: 0;
    list-style: none;
  }
  .contact__row {
    display: flex;
    height: 37px;
    margin-bottom: 13px;
  }
  .contact__label {
    width: 160px;
    background: var(--pink);
    color: var(--white);
    font-size: 20px;
    letter-spacing: 1px;
    line-height: 37px;
    text-align: center;
  }
  .contact__value {
    width: 440px;
    background: var(--value-bg);
    color: var(--white);
    font-size: 20px;
    letter-spacing: 1.2px;
    line-height: 37px;
    padding-left: 18px;
    box-sizing: border-box;
    white-space: nowrap;
  }
  .contact-icon {
    position: absolute;
    width: 34px;
    height: 34px;
  }
  .contact-icon--phone { left: 443px; top: 386px; }
  .contact-icon--web { left: 443px; top: 453px; }
</style>
</head>
<body>
  <main class="card">
    <svg class="card__frame" viewBox="0 0 1110 685" preserveAspectRatio="none" aria-hidden="true">
      <rect class="frame-left-band" x="0" y="0" width="66" height="685" fill="var(--pink)"/>
      <polygon class="frame-right-dark" points="1000,0 1110,0 1110,685 1040,685" fill="var(--edge-dark)"/>
      <polygon class="frame-right-stripe" points="1000,0 1036,0 1066,685 1040,685" fill="var(--pink)"/>
      <polygon class="frame-right-band" points="1058,0 1110,0 1110,685 1088,685" fill="var(--pink)"/>
    </svg>

    <h1 class="brand-name brand-name--header">VELVET &amp; BLOOM</h1>

    <div class="brand-mark">
      <span class="brand-mark__dot"></span>
      <p class="brand-name">VELVET &amp; BLOOM</p>
    </div>

    <p class="tagline">“PREMIUM HAIR FOR EVERY MOMENT!”</p>

    <svg class="contact-icon contact-icon--phone" viewBox="0 0 24 24" aria-hidden="true">
      <path fill="var(--grey)" d="M6.6 10.8c1.4 2.8 3.8 5.1 6.6 6.6l2.2-2.2c.3-.3.7-.4 1-.2 1.1.4 2.3.6 3.6.6.6 0 1 .4 1 1V20c0 .6-.4 1-1 1C10.6 21 3 13.4 3 4c0-.6.4-1 1-1h3.5c.6 0 1 .4 1 1 0 1.3.2 2.5.6 3.6.1.3 0 .7-.2 1z"/>
    </svg>
    <svg class="contact-icon contact-icon--web" viewBox="0 0 24 24" aria-hidden="true">
      <g fill="none" stroke="var(--grey)" stroke-width="1.6">
        <circle cx="12" cy="12" r="9.5"/>
        <ellipse cx="12" cy="12" rx="4.2" ry="9.5"/>
        <line x1="2.5" y1="12" x2="21.5" y2="12"/>
        <line x1="4" y1="7" x2="20" y2="7"/>
        <line x1="4" y1="17" x2="20" y2="17"/>
        <line x1="12" y1="2.5" x2="12" y2="21.5"/>
      </g>
    </svg>

    <ul class="contact">
      <li class="contact__row">
        <span class="contact__label">PHONE:</span>
        <span class="contact__value">44 07391 XXXXXXX</span>
      </li>
      <li class="contact__row">
        <span class="contact__label">E-MAIL:</span>
        <span class="contact__value">INFO@VELVETANDBLOOM-DEMO.COM</span>
      </li>
      <li class="contact__row">
        <span class="contact__label">WEBSITE:</span>
        <span class="contact__value">WWW.VELVETANDBLOOM-DEMO.COM</span>
      </li>
    </ul>
  </main>
</body>
</html>
```